Talvick Industrial Maintenance Business Card

Design a business card with the following information, logo must be included.
Talvick Industrial Maintenance
Dan Pelfrey Jr.
Pone 555-214-7608
email dan.pelfrey.jr@mailvantor.com

```html
<!DOCTYPE html>
<html lang="en">
<head>
<meta charset="utf-8">
<title>Talvick Industrial Maintenance – Business Card</title>
<link rel="stylesheet" href="https://fonts.googleapis.com/css2?family=Montserrat:wght@500;700&display=swap">
<style>
  :root {
    --brand-blue: #1a73bd;
    --brand-navy: #2c4b93;
    --ink-grey: #6f6f6f;
    --paper: #ffffff;
    --backdrop: #e9eaec;
  }
  * { box-sizing: border-box; margin: 0; padding: 0; }
  html, body { width: 1200px; height: 913px; overflow: hidden; }
  body {
    background: var(--backdrop);
    font-family: "Montserrat", sans-serif;
    position: relative;
  }
  .card {
    position: absolute;
    left: 270px;
    width: 660px;
    height: 377px;
    border-radius: 22px;
    overflow: hidden;
    box-shadow: 0 6px 18px rgba(0,0,0,0.18);
  }
  .card--back { top: 48px; background: var(--brand-blue); }
  .card--front { top: 478px; background: var(--paper); }

  .wordmark {
    display: flex;
    align-items: center;
    gap: 14px;
    font-weight: 700;
    text-transform: uppercase;
    line-height: 1.05;
  }
  .wordmark__dot { border-radius: 50%; flex: none; }

  .card--back .wordmark {
    position: absolute;
    left: 50%; top: 50%;
    transform: translate(-50%, -50%);
    color: var(--brand-navy);
    font-size: 30px;
    letter-spacing: 1px;
  }
  .card--back .wordmark__dot { width: 58px; height: 58px; background: var(--brand-navy); }
  .card--back .wordmark__text span { display: block; font-size: 30px; }

  .card--front .wordmark {
    position: absolute;
    left: 46px; top: 70px;
    color: var(--brand-blue);
  }
  .card--front .wordmark__text span { display: block; font-size: 34px; letter-spacing: 1px; }
  .card--front .wordmark__text small { display: block; font-size: 13.5px; letter-spacing: 0.6px; margin-top: 4px; }
  .card--back .wordmark__text small { display: block; font-size: 12px; letter-spacing: 0.6px; margin-top: 4px; }

  .emblem {
    position: absolute;
    right: 28px; top: 44px;
    width: 270px; height: 270px;
  }

  .contact-name {
    position: absolute;
    left: 88px; top: 214px;
    color: var(--brand-blue);
    font-weight: 700;
    font-size: 22px;
    letter-spacing: 0.5px;
    text-transform: uppercase;
  }
  .contact-list {
    position: absolute;
    left: 88px; top: 268px;
    list-style: none;
    color: var(--ink-grey);
    font-weight: 500;
    font-size: 16px;
  }
  .contact-list li { display: flex; align-items: center; gap: 10px; margin-bottom: 10px; }
  .contact-list svg { width: 16px; height: 16px; fill: var(--brand-blue); flex: none; }
</style>
</head>
<body>

<section class="card card--back" aria-label="Card back">
  <div class="wordmark">
    <span class="wordmark__dot"></span>
    <div class="wordmark__text">
      <span>Talvick</span>
      <small>Industrial Maintenance</small>
    </div>
  </div>
</section>

<section class="card card--front" aria-label="Card front">
  <div class="wordmark">
    <div class="wordmark__text">
      <span>Talvick</span>
      <small>Industrial Maintenance</small>
    </div>
  </div>

  <svg class="emblem" viewBox="0 0 270 270" aria-hidden="true">
    <circle cx="135" cy="135" r="112" fill="none" stroke="var(--brand-blue)" stroke-width="30"/>
  </svg>

  <p class="contact-name">Dan Pelfrey Jr.</p>
  <ul class="contact-list">
    <li>
      <svg viewBox="0 0 24 24" aria-hidden="true"><path d="M6.6 10.8a15.1 15.1 0 0 0 6.6 6.6l2.2-2.2a1 1 0 0 1 1-.25 11.4 11.4 0 0 0 3.6.57 1 1 0 0 1 1 1V20a1 1 0 0 1-1 1A17 17 0 0 1 3 4a1 1 0 0 1 1-1h3.5a1 1 0 0 1 1 1c0 1.25.2 2.45.57 3.57a1 1 0 0 1-.25 1z"/></svg>
      555-214-7608
    </li>
    <li>
      <svg viewBox="0 0 24 24" aria-hidden="true"><path d="M2 5h20v14H2z M2 5l10 8 10-8" fill="var(--brand-blue)" stroke="#fff" stroke-width="1.5"/></svg>
      dan.pelfrey.jr@mailvantor.com
    </li>
  </ul>
</section>

</body>
</html>
```